Tembo & Lusani Advocates website

An interactive professional law firm website fully synchronized with social media pages.

Target Market(s)

Corporations and professionals

Industry/Entity Type

Professional Service

Number of Pages Required

5+ page

Font styles to use
Sans Serif

Colors

Designer to choose colors to be used in the design.

```html
<!DOCTYPE html>
<html lang="en">
<head>
<meta charset="utf-8">
<title>Tembo &amp; Lusani Advocates</title>
<link rel="stylesheet" href="https://fonts.googleapis.com/css2?family=Sorts+Mill+Goudy&family=Montserrat:wght@400&display=swap">
<style>
  :root {
    --ink-dark: #0b0b0c;
    --slate: #3a3b3f;
    --mist: #8f8e8f;
    --window-light: #e9e4d6;
    --warm-glow: #c98a62;
    --band-red: rgba(150, 62, 52, 0.55);
    --brand-red: #a23a36;
    --rule: rgba(255, 255, 255, 0.22);
    --text-light: #f1ebe6;
    --text-soft: #e6ddd6;
  }
  * { margin: 0; padding: 0; box-sizing: border-box; }
  html, body { width: 1200px; height: 675px; overflow: hidden; background: var(--ink-dark); }
  .hero {
    position: relative;
    width: 1200px;
    height: 675px;
    overflow: hidden;
    font-family: "Sorts Mill Goudy", Georgia, serif;
    color: var(--text-light);
  }
  .hero-photo {
    position: absolute;
    inset: 0;
    background:
      radial-gradient(ellipse 260px 200px at 930px 90px, rgba(233, 228, 214, 0.75), transparent 70%),
      radial-gradient(ellipse 200px 160px at 830px 230px, rgba(201, 138, 98, 0.55), transparent 70%),
      linear-gradient(160deg, #3b3a3d 0%, #4a4a4f 45%, #6f6e72 70%, #8a8a8d 100%);
  }
  .hero-shade {
    position: absolute;
    inset: 0;
    background:
      linear-gradient(90deg, rgba(0,0,0,0.95) 0%, rgba(0,0,0,0.55) 10%, rgba(0,0,0,0.25) 30%, rgba(0,0,0,0) 60%),
      linear-gradient(180deg, rgba(0,0,0,0.35) 0%, rgba(0,0,0,0) 30%, rgba(0,0,0,0.15) 75%, rgba(0,0,0,0.45) 100%);
  }
  .brand {
    position: absolute;
    left: 74px;
    top: 40px;
    width: 340px;
  }
  .brand-name {
    display: flex;
    align-items: center;
    gap: 12px;
    font-size: 25px;
    line-height: 1.05;
    color: var(--text-light);
    padding-bottom: 20px;
    border-bottom: 1px solid var(--rule);
  }
  .brand-mark {
    width: 14px;
    height: 14px;
    background: var(--brand-red);
    flex: none;
  }
  .brand-tagline {
    margin-top: 9px;
    padding-left: 4px;
    font-family: "Montserrat", Arial, sans-serif;
    font-size: 7.5px;
    letter-spacing: 2.6px;
    color: var(--brand-red);
    white-space: nowrap;
  }
  .intro-band {
    position: absolute;
    left: 0;
    top: 205px;
    width: 1186px;
    height: 267px;
    background: linear-gradient(90deg, rgba(110, 45, 40, 0.55) 0%, var(--band-red) 55%, rgba(170, 110, 100, 0.35) 100%);
  }
  .intro-title {
    position: absolute;
    left: 66px;
    top: 230px;
    font-size: 36px;
    font-weight: 400;
    color: var(--text-light);
  }
  .intro-text {
    position: absolute;
    left: 66px;
    top: 302px;
    width: 650px;
    font-size: 16.6px;
    line-height: 27.3px;
    color: var(--text-soft);
  }
  .practice-nav {
    position: absolute;
    left: 66px;
    top: 499px;
    display: flex;
    gap: 38px;
    list-style: none;
    font-size: 17.5px;
    text-transform: uppercase;
    color: var(--text-soft);
  }
</style>
</head>
<body>
  <main class="hero">
    <div class="hero-photo" role="img" aria-label="Photo of a professional in a suit seated on a grey sofa, holding a tablet and stylus beside a bright window"></div>
    <div class="hero-shade"></div>

    <header class="brand">
      <div class="brand-name">
        <span class="brand-mark"></span>
        <span>Tembo &amp; Lusani Advocates</span>
      </div>
      <p class="brand-tagline">CONSTRUCTION LAW &nbsp;|&nbsp; ARBITRATION &nbsp;|&nbsp; LITIGATION</p>
    </header>

    <div class="intro-band"></div>
    <h1 class="intro-title">Tembo &amp; Lusani Advocates</h1>
    <p class="intro-text">Tembo &amp; Lusani Advocates are a specialist commercial law firm in Uganda focusing on commercial litigation, construction law and arbitration. We have excelled in our niche areas for over two decades and we continue to grow and be the firm choice in those practice areas.</p>

    <ul class="practice-nav">
      <li>Construction Law</li>
      <li>Arbitration</li>
      <li>Litigation</li>
    </ul>
  </main>
</body>
</html>
```